BrindleStaffing Business Card Design

We are a staffing company finding positions for dedicated nurses and physicians.

Target Market(s)

Business Professionals

Industry/Entity Type

Staffing

Contact Information for Business Card

Gregory Malden
Chairman
417 39th Crescent South
SAINT PETERSBURG FL 33719
813-555-0147 Mobile
813-555-0183 Fax
gmalden@brindlestaffing.example
www.brindlestaffing.example

Font styles to use
Sans Serif

Colors
fbee3e
f04a50
f37122

Requirements
Must have
• Logo Attached, see colors below. We'd like to see Yellow, Orange and Red.

```html
<!DOCTYPE html>
<html lang="en">
<head>
<meta charset="utf-8">
<title>BrindleStaffing Business Card</title>
<link rel="stylesheet" href="https://fonts.googleapis.com/css2?family=Roboto:wght@400;500;700&display=swap">
<style>
  :root {
    --backdrop: #dcdcdc;
    --card: #ffffff;
    --brand-yellow: #fbee3e;
    --brand-orange: #f37122;
    --brand-red: #f04a50;
    --ink: #555a5e;
  }
  * { margin: 0; padding: 0; box-sizing: border-box; }
  html, body {
    width: 1125px; height: 1200px; overflow: hidden;
    background: var(--backdrop);
    font-family: "Roboto", Arial, sans-serif;
  }
  .canvas { position: relative; width: 1125px; height: 1200px; }
  .card {
    position: absolute; left: 150px; width: 825px; height: 471px;
    background: var(--card);
  }
  .card--front { top: 98px; }
  .card--back { top: 631px; }

  .accent-bar {
    position: absolute; left: 0; top: 90px; width: 24px; height: 60px;
    background: var(--brand-red);
  }
  .person { position: absolute; left: 61px; top: 88px; }
  .person__name {
    font-size: 30px; font-weight: 700; color: var(--brand-orange); line-height: 1.1;
  }
  .person__title {
    font-size: 20px; font-weight: 500; color: var(--brand-red); line-height: 1.2;
  }
  .address {
    position: absolute; left: 61px; top: 229px;
    font-style: normal;
    font-size: 20px; color: var(--ink); line-height: 26px;
  }
  .contact-list {
    position: absolute; left: 61px; top: 295px; list-style: none;
  }
  .contact-list li {
    display: flex; align-items: center; height: 26.3px;
    font-size: 20px; color: var(--ink);
  }
  .contact-list svg { width: 20px; height: 20px; margin-right: 13px; flex: none; }
  .cross { position: absolute; left: 0; top: 0; }

  .wordmark {
    position: absolute; left: 0; right: 0; top: 205px;
    text-align: center;
    font-size: 78px; font-weight: 700;
    color: var(--brand-orange); line-height: 90px;
  }
</style>
</head>
<body>
<main class="canvas">
  <section class="card card--front">
    <div class="accent-bar"></div>
    <div class="person">
      <h1 class="person__name">Gregory Malden</h1>
      <p class="person__title">Chairman</p>
    </div>
    <address class="address">
      417 39th Crescent South<br>
      SAINT PETERSBURG FL 33719
    </address>
    <ul class="contact-list">
      <li>
        <svg viewBox="0 0 20 20" aria-hidden="true"><rect x="5" y="1" width="10" height="18" rx="2" fill="none" stroke="var(--brand-orange)" stroke-width="2"/><circle cx="10" cy="15.5" r="1.2" fill="var(--brand-orange)"/></svg>
        813-555-0147
      </li>
      <li>
        <svg viewBox="0 0 20 20" aria-hidden="true"><rect x="5" y="2" width="10" height="6" fill="var(--brand-orange)"/><rect x="1" y="8" width="18" height="8" rx="2" fill="var(--brand-orange)"/><rect x="5" y="13" width="10" height="5" fill="#fff" stroke="var(--brand-orange)" stroke-width="1.5"/></svg>
        813-555-0183
      </li>
      <li>
        <svg viewBox="0 0 20 20" aria-hidden="true"><rect x="1" y="4" width="18" height="12" fill="var(--brand-orange)"/><path d="M2 5 L10 11 L18 5" fill="none" stroke="#fff" stroke-width="1.5"/></svg>
        gmalden@brindlestaffing.example
      </li>
      <li>
        <svg viewBox="0 0 20 20" aria-hidden="true"><circle cx="10" cy="10" r="9" fill="var(--brand-orange)"/><path d="M5 5 Q8 7 7 10 Q9 12 8 16 M12 3 Q11 6 14 8 Q17 9 16 13" fill="none" stroke="#fff" stroke-width="1.6"/></svg>
        www.brindlestaffing.example
      </li>
    </ul>
    <svg class="cross" width="825" height="471" viewBox="0 0 825 471" aria-hidden="true">
      <path fill="var(--brand-yellow)" d="M522 68 H669 V172 H779 V311 H669 V415 H522 V311 H412 V172 H522 Z"/>
    </svg>
  </section>

  <section class="card card--back">
    <p class="wordmark">BrindleStaffing</p>
  </section>
</main>
</body>
</html>
```